Business cards for Marrowfield Consulting with the following info for the front side:

Marrowfield Consulting
Executive Coaching and Human Capital Strategy
www.marrowfield.example

Idalia Renvoort
Principal
idalia@marrowfield.example
+1 555 274 9186

Black background, text using the colours of the logo - enclosed.

The back side of the business card should feature the logo in the middle, with "Executive Coaching and Human Capital Strategy" on top and "www.marrowfield.example" below.

```html
<!DOCTYPE html>
<html lang="en">
<head>
<meta charset="utf-8">
<title>Marrowfield Consulting – Business Cards</title>
<link rel="stylesheet" href="https://fonts.googleapis.com/css2?family=Montserrat:wght@400;500;600;700&display=swap">
<style>
  :root {
    --stage: #2a2a2b;
    --card: #0e0f12;
    --blue: #2aa7df;
    --yellow: #f6c21c;
  }
  * { margin: 0; padding: 0; box-sizing: border-box; }
  html, body {
    width: 1200px;
    height: 1000px;
    overflow: hidden;
    background: var(--stage);
    font-family: "Montserrat", sans-serif;
  }
  .stage {
    width: 1200px;
    height: 1000px;
    display: flex;
    flex-direction: column;
    align-items: center;
    justify-content: center;
    gap: 56px;
  }
  .card {
    position: relative;
    width: 700px;
    height: 400px;
    background: var(--card);
    border-radius: 22px;
    box-shadow: 0 18px 40px rgba(0,0,0,0.45);
    overflow: hidden;
  }

  /* Back side */
  .card--back {
    display: flex;
    flex-direction: column;
    align-items: center;
    justify-content: center;
  }
  .tagline {
    position: absolute;
    top: 78px;
    left: 0; right: 0;
    text-align: center;
    color: var(--blue);
    font-size: 18px;
    font-weight: 500;
    letter-spacing: 0.5px;
  }
  .brand {
    display: flex;
    align-items: center;
    gap: 16px;
  }
  .brand__mark { flex: none; }
  .brand__name {
    color: var(--blue);
    font-weight: 600;
    letter-spacing: 1px;
    line-height: 1;
  }
  .brand--large .brand__name { font-size: 52px; }
  .site-url {
    position: absolute;
    bottom: 78px;
    left: 0; right: 0;
    text-align: center;
    color: var(--yellow);
    font-size: 18px;
    font-weight: 500;
    letter-spacing: 0.5px;
  }

  /* Front side */
  .card--front .brand {
    position: absolute;
    left: 40px;
    top: 150px;
    gap: 10px;
  }
  .brand--small .brand__name { font-size: 30px; }
  .divider {
    position: absolute;
    left: 372px;
    top: 110px;
    width: 2px;
    height: 180px;
    background: var(--yellow);
  }
  .contact {
    position: absolute;
    left: 400px;
    top: 128px;
  }
  .contact__name {
    color: var(--yellow);
    font-size: 25px;
    font-weight: 700;
    letter-spacing: 0.5px;
  }
  .contact__role {
    color: var(--blue);
    font-size: 18px;
    font-weight: 500;
    margin-top: 2px;
  }
  .contact__list {
    list-style: none;
    margin-top: 22px;
  }
  .contact__item {
    display: flex;
    align-items: center;
    gap: 9px;
    color: var(--blue);
    font-size: 17px;
    font-weight: 500;
    line-height: 1.65;
    letter-spacing: 0.3px;
  }
  .contact__icon { flex: none; }
</style>
</head>
<body>
<main class="stage">

  <section class="card card--back" aria-label="Business card, back side">
    <p class="tagline">Executive Coaching and Human Capital Strategy</p>
    <div class="brand brand--large">
      <svg class="brand__mark" width="62" height="62" viewBox="0 0 62 62" aria-hidden="true">
        <circle cx="31" cy="31" r="28" fill="none" stroke="var(--yellow)" stroke-width="4"/>
      </svg>
      <span class="brand__name">MARROWFIELD</span>
    </div>
    <p class="site-url">www.marrowfield.example</p>
  </section>

  <section class="card card--front" aria-label="Business card, front side">
    <div class="brand brand--small">
      <svg class="brand__mark" width="40" height="40" viewBox="0 0 40 40" aria-hidden="true">
        <circle cx="20" cy="20" r="17.5" fill="none" stroke="var(--yellow)" stroke-width="3"/>
      </svg>
      <span class="brand__name">MARROWFIELD</span>
    </div>

    <div class="divider" aria-hidden="true"></div>

    <div class="contact">
      <h1 class="contact__name">Idalia Renvoort</h1>
      <p class="contact__role">Principal</p>
      <ul class="contact__list">
        <li class="contact__item">
          <svg class="contact__icon" width="14" height="14" viewBox="0 0 24 24" aria-hidden="true">
            <path fill="var(--blue)" d="M6.6 10.8a15.1 15.1 0 0 0 6.6 6.6l2.2-2.2a1 1 0 0 1 1-.25 11.4 11.4 0 0 0 3.6.57 1 1 0 0 1 1 1V20a1 1 0 0 1-1 1A17 17 0 0 1 3 4a1 1 0 0 1 1-1h3.5a1 1 0 0 1 1 1c0 1.25.2 2.45.57 3.57a1 1 0 0 1-.25 1z"/>
          </svg>
          <span>+1 555 274 9186</span>
        </li>
        <li class="contact__item">
          <svg class="contact__icon" width="14" height="14" viewBox="0 0 24 24" aria-hidden="true">
            <path fill="var(--blue)" d="M2 5h20v14H2z M4 7v.4l8 5.2 8-5.2V7z" fill-rule="evenodd"/>
          </svg>
          <span>idalia@marrowfield.example</span>
        </li>
        <li class="contact__item">
          <svg class="contact__icon" width="14" height="14" viewBox="0 0 24 24" aria-hidden="true">
            <g fill="none" stroke="var(--blue)" stroke-width="2">
              <circle cx="12" cy="12" r="10"/>
              <ellipse cx="12" cy="12" rx="4.5" ry="10"/>
              <path d="M2 12h20M4 7h16M4 17h16"/>
            </g>
          </svg>
          <span>www.marrowfield.example</span>
        </li>
      </ul>
    </div>
  </section>

</main>
</body>
</html>
```